Marco Delvane 'wait for june' CD cover design

Design a CD cover and a logo (using my initials- MD)
Basically the two files attached are what I'm looking for (front and back)
I'd like my image to stand out with a white background.
The logo will be something I use on all my albums and website.
I like the white bold look.
Possible enhance image marginally I've lost a little weight since taking the picture.
The music I perform is Jazz Swing

Target Market(s)

Jazz Swing Audience

```html
<!DOCTYPE html>
<html lang="en">
<head>
<meta charset="utf-8">
<title>Marco Delvane – wait for june</title>
<link rel="stylesheet" href="https://fonts.googleapis.com/css2?family=Archivo+Black&family=Exo+2:wght@700&display=swap">
<style>
  :root {
    --paper: #f2f2f2;
    --sky-light: #f7f7f7;
    --sky-mid: #d2d2d2;
    --sky-dark: #9a9a9a;
    --ground: #c4c4c4;
    --title-lime: #b9d23a;
    --title-lime-dark: #7e9a16;
    --numeral-grey: #3c3c3c;
    --ink: #111111;
    --photo-top: #e6e6e6;
    --photo-mid: #8a8a8a;
    --photo-dark: #1f1f1f;
  }
  * { margin: 0; padding: 0; box-sizing: border-box; }
  html, body { width: 1200px; height: 1200px; overflow: hidden; background: var(--paper); }
  .cover {
    position: relative;
    width: 1200px;
    height: 1200px;
    overflow: hidden;
    background: var(--paper);
  }
  .cover__landscape {
    position: absolute;
    inset: 0;
    background: linear-gradient(180deg, var(--sky-dark) 0%, var(--sky-mid) 20%, var(--sky-light) 46%, #e8e8e8 72%, var(--ground) 100%);
  }
  .cover__portrait {
    position: absolute;
    left: 640px;
    top: 330px;
    width: 520px;
    height: 870px;
    border-radius: 220px 220px 0 0;
    background: linear-gradient(180deg, var(--photo-top) 0%, var(--photo-mid) 30%, var(--photo-dark) 58%, var(--photo-dark) 100%);
  }
  .brand-mark {
    position: absolute;
    top: 100px;
    right: 90px;
    font-family: "Archivo Black", sans-serif;
    font-size: 44px;
    line-height: 1;
    color: var(--ink);
    letter-spacing: -1px;
  }
  .album-title {
    position: absolute;
    left: 40px;
    top: 300px;
  }
  .album-title__line {
    display: block;
    font-family: "Exo 2", sans-serif;
    font-weight: 700;
    font-size: 92px;
    line-height: 1;
    color: var(--title-lime);
    background: linear-gradient(180deg, var(--title-lime) 0%, var(--title-lime-dark) 100%);
    -webkit-background-clip: text;
    background-clip: text;
    -webkit-text-fill-color: transparent;
    letter-spacing: 1px;
  }
  .album-title__word {
    display: block;
    margin: 14px 0 0 150px;
    font-family: "Archivo Black", sans-serif;
    font-size: 120px;
    line-height: 1;
    color: var(--numeral-grey);
    letter-spacing: -2px;
  }
  .artist-name {
    position: absolute;
    left: 90px;
    top: 620px;
    font-family: "Archivo Black", sans-serif;
    font-size: 58px;
    line-height: 1;
    color: var(--ink);
    letter-spacing: -1px;
  }
</style>
</head>
<body>
  <main class="cover">
    <div class="cover__landscape" role="img" aria-label="Black and white snowy landscape under a cloudy sky"></div>
    <div class="cover__portrait" role="img" aria-label="Portrait photograph of the artist in a black suit, white shirt and black tie"></div>
    <div class="brand-mark">MD</div>
    <h1 class="album-title">
      <span class="album-title__line">wait for</span>
      <span class="album-title__word">june</span>
    </h1>
    <p class="artist-name">Marco Delvane</p>
  </main>
</body>
</html>
```